Brantley Estates is a commercial real estate development company based in the United States. We develop high-end office buildings and student housing apartments. We have a new logo and need to update all of our stationary items and business cards. We would like the design to be clean and professional. Our logo and color information is attached. Our logo MUST be in full color and not as white. It is preferred that the logo is on a white background.

Color code Blue R 0. G 62. B 124 ( #003E7C )
C 100 M84 Y 26 K 22
Black R32. G30. B30 ( #201E1E)
C100 M100 Y100 K100

Font used TRAJAN PRO3 PRO BOLD.

Items needed:
1. Business card - Leaning towards doing just a one side business card in a thicker paper. Include - logo, name - Martin E. Caldwell, Title - Chairman & CEO, 5120 Ridgemont Pkwy. Suite 400, Atlanta, GA 30327 - Cell number 404.617.####, Office 770.245.62## email@brantleyestates.com; www.brantleyestates.com.

2. Letterhead - Standard 8.5 by 11 paper. We do have a smaller size for the CEO that is 7.25 by 10.5 that is just a mirror of the letterhead except with his name (Martin E. Caldwell) and title (Chariman & CEO) listed at the top in the header. Letthead needs address, phone number and website, plus logo. *Prepared such that we can either implement as a Google Document template or professionally print.

3. Legal sized envelope - #10 envelope - which measures 4 1/8" by 9 1/2". We also use the same size envelope with a window. Need logo and address. A photo of the old envelope style is attached.

4. 9" x 12" Pocket folder - Need a design that can also be split to be a cover page and back - We use the cover pages in spiral binding machine, so we need to leave room on the left for that. One of the pockets should hold a business card. Include logo, address, phone, website. Also if text is needed, we could say development / leasing / property management.

5. Shipping label - 3 1/3" x 4" inches and 6 per page. Just need logo and address listed at top of the label and white space at bottom.

Company: Brantley Estates
Address: 5120 Ridgemont Pkwy. Suite 400, Atlanta, GA 30327
Phone: 770.245.6274
Fax: 770.245.6219 (probably not needed)
Website: www.brantleyestates.com

Thank you for all your help!

Target Market(s)

Should communicate a strong corporate feel

Contact Information for Business Card

Include - logo, name - Martin E. Caldwell, Title - Chairman & CEO, 5120 Ridgemont Pkwy. Suite 400, Atlanta, GA 30327 - Cell number 404.617.####, Office 770.245.62## email@brantleyestates.com; www.brantleyestates.com.

Logo Text

Brantley Estates

Colors

Designer to choose colors to be used in the design.

Requirements
Must have
• Our logo MUST be in full color and not as white. It is preferred that the logo is on a white background.
• Colors - Color code Blue R 0. G 62. B 124 ( #003E7C )
• C 100 M84 Y 26 K 22
Nice to have
• Font used in logo TRAJAN PRO3 PRO BOLD. Would love to see options of both a one sided and double-sided.
Should not have
• Logo in white.

```html
<!DOCTYPE html>
<html lang="en">
<head>
<meta charset="utf-8">
<title>Brantley Estates — Business Card</title>
<link rel="stylesheet" href="https://fonts.googleapis.com/css2?family=Cinzel:wght@700&family=EB+Garamond:wght@400;500&display=swap">
<style>
  :root {
    --brand-blue: #003e7c;
    --panel-blue: #1d3f74;
    --ink-black: #201e1e;
    --ink-grey: #4a4a4a;
    --paper: #ffffff;
    --backdrop: #2b2b2d;
  }
  * { box-sizing: border-box; margin: 0; padding: 0; }
  html, body {
    width: 1200px; height: 1108px; overflow: hidden;
    background: var(--backdrop);
  }
  .canvas {
    position: relative; width: 1200px; height: 1108px;
  }
  .card {
    position: absolute; left: 220px; width: 760px; height: 434px;
    background: var(--paper);
    box-shadow: 0 18px 40px rgba(0,0,0,0.45);
    overflow: hidden;
  }
  .card--front { top: 60px; }
  .card--back { top: 594px; }

  /* Front */
  .front-lockup {
    position: absolute; left: 0; right: 0; top: 150px;
    display: flex; align-items: center; justify-content: center; gap: 18px;
  }
  .brand-dot {
    width: 58px; height: 58px; border-radius: 50%;
    background: var(--brand-blue);
  }
  .brand-name {
    font-family: "Cinzel", serif; font-weight: 700;
    color: var(--brand-blue);
    font-size: 44px; letter-spacing: 2px; line-height: 1;
  }
  .front-web {
    position: absolute; left: 0; right: 0; top: 290px; text-align: center;
    font-family: "EB Garamond", serif; font-size: 20px;
    letter-spacing: 5px; color: var(--ink-grey);
  }

  /* Back */
  .back-panel { position: absolute; inset: 0; }
  .back-brand {
    position: absolute; left: 46px; top: 40px;
    font-family: "Cinzel", serif; font-weight: 700;
    color: var(--brand-blue); font-size: 34px; letter-spacing: 1.5px; line-height: 1;
  }
  .person { position: absolute; left: 46px; top: 104px; }
  .person-name {
    font-family: "Cinzel", serif; font-weight: 700;
    color: var(--brand-blue); font-size: 24px; letter-spacing: 1px;
  }
  .person-title {
    font-family: "EB Garamond", serif; font-size: 17px;
    color: var(--ink-black); letter-spacing: 1px; text-transform: uppercase;
  }
  .address {
    position: absolute; left: 46px; top: 172px;
    font-family: "EB Garamond", serif; font-size: 17px; line-height: 1.35;
    color: var(--ink-grey);
  }
  .contacts {
    position: absolute; left: 46px; top: 236px; list-style: none;
    font-family: "EB Garamond", serif; font-size: 17px; line-height: 1.55;
    color: var(--ink-grey);
  }
  .contacts li { display: flex; align-items: center; gap: 10px; }
  .contacts svg { width: 15px; height: 15px; fill: var(--brand-blue); flex: none; }
</style>
</head>
<body>
<main class="canvas">

  <section class="card card--front" aria-label="Business card front">
    <div class="front-lockup">
      <span class="brand-dot" aria-hidden="true"></span>
      <span class="brand-name">Brantley Estates</span>
    </div>
    <p class="front-web">www.brantleyestates.com</p>
  </section>

  <section class="card card--back" aria-label="Business card back">
    <svg class="back-panel" viewBox="0 0 760 434" aria-hidden="true">
      <polygon points="545,90 760,90 760,434 520,434 470,260" fill="var(--panel-blue)"/>
    </svg>

    <div class="back-brand">Brantley Estates</div>

    <div class="person">
      <p class="person-name">Martin E. Caldwell</p>
      <p class="person-title">Chairman, CEO</p>
    </div>

    <p class="address">5120 Ridgemont Pkwy.<br>Suite 400, Atlanta, GA 30327</p>

    <ul class="contacts">
      <li>
        <svg viewBox="0 0 16 16"><path d="M3 1l3 3-1.5 2a9 9 0 0 0 5.5 5.5L12 10l3 3-2 2C7 15 1 9 1 3z"/></svg>
        770.245.6274
      </li>
      <li>
        <svg viewBox="0 0 16 16"><path d="M4 0h8v16H4zM5.5 2v10h5V2zM7 13.5h2v1H7z" fill-rule="evenodd"/></svg>
        404.617.8852
      </li>
      <li>
        <svg viewBox="0 0 16 16"><path d="M0 3h16v10H0zM1.5 4.5l6.5 5 6.5-5v-.5h-13z"/></svg>
        email@brantleyestates.com
      </li>
      <li>
        <svg viewBox="0 0 16 16"><circle cx="8" cy="8" r="7"/></svg>
        www.brantleyestates.com
      </li>
    </ul>
  </section>

</main>
</body>
</html>
```